Modern Venture Capital website

Design a modern website for a venture capital firm. This website should be modern and beautiful and be on par with other Venture Capital websites. I have a logo and a hero video I'd like to use. Link to hero video: https://files.vantoria.example/f/9Xk2Lm7qPz4Rt8Wb3Nc6Hd5Jy1Gs0Ve/view?ref=share_link

Preference will be given to the best design that combines design with the best images and digital content. That means no generic free stock videos 😅

I currently built a wix website to give you an idea of what content needs to be on the website. Depending on your design it can be 3 pages, or one long page. I will leave it up to you.

WEBSITE: https://brelmor58204.pagecraftly.example/my-site-4

Target Market(s)

Mid-career professionals, individuals interested in Venture Capital

Industry/Entity Type

Finance, venture capital, startups

Requirements
Must have
• must use the hero video I have and must use my logo. Must use high quality images that matches the website design - no generic stock images

```html
<!DOCTYPE html>
<html lang="en">
<head>
<meta charset="utf-8">
<title>Nocturne Ventures — Venture Capital for the late night hustlers</title>
<link href="https://fonts.googleapis.com/css2?family=Outfit:wght@300;400;500;600;700&display=swap" rel="stylesheet">
<style>
:root{
  --bg:#0b0b0c;
  --card:#26262c;
  --text:#ffffff;
  --muted:#b9b9bf;
  --accent:#ff5a2b;
  --ring:#c4c4c4;
  --line:#2c2c30;
  --icon-light:#e6e6e6;
  --icon-mid:#a9a9a9;
  --icon-dark:#6f6f6f;
}
*{box-sizing:border-box;margin:0;padding:0}
html,body{width:1200px;height:3797px;overflow:hidden;background:var(--bg)}
body{font-family:"Outfit",sans-serif;color:var(--text);position:relative}
.page{position:relative;width:1200px;height:3797px;overflow:hidden}
.backdrop{position:absolute;inset:0}
.abs{position:absolute}
.center{text-align:center}
.btn{display:inline-flex;align-items:center;justify-content:center;background:var(--accent);color:#fff;border-radius:20px;font-size:12px;font-weight:500;text-decoration:none}

/* nav */
.nav-logo{left:93px;top:18px;font-size:32px;font-weight:700;letter-spacing:-.5px;line-height:1}
.nav-logo small{display:block;font-size:10px;letter-spacing:4px;font-weight:600;margin-top:2px}
.nav-links{top:30px;font-size:12px;font-weight:500;line-height:16px}
.nav-cta{left:996px;top:20px;width:111px;height:38px;border:1.5px solid #fff;border-radius:20px;display:flex;align-items:center;justify-content:center;font-size:12px;font-weight:500}

/* hero */
.hero-title{left:0;width:1200px;top:196px;font-size:52px;font-weight:700;line-height:56px}
.hero-sub{left:0;width:1200px;top:326px;font-size:18px;font-weight:400}
.hero-btn{left:545px;top:364px;width:110px;height:34px}

/* become card */
.become-card{left:315px;top:631px;width:569px;height:355px;border-radius:32px;background:linear-gradient(160deg,#1d1d22 0%,#2a2a31 55%,#34343a 100%);overflow:hidden}
.become-glow{position:absolute;inset:0;background:radial-gradient(ellipse 60% 30% at 45% 45%,rgba(70,90,200,.35),transparent 70%)}
.become-title{position:absolute;left:0;right:0;top:105px;font-size:28px;font-weight:700}
.become-text{position:absolute;left:82px;right:82px;top:146px;font-size:15px;line-height:23px;font-weight:400}

/* features */
.feature-icon{width:110px;height:110px;border-radius:50%;margin:0 auto;background:linear-gradient(180deg,var(--icon-light),var(--icon-mid) 60%,var(--icon-dark))}
.feature{width:220px;text-align:center}
.feature h3{font-size:16px;font-weight:700;line-height:22px;margin-top:16px}
.feature-lead{width:380px;text-align:center}
.feature-lead h3{font-size:16px;font-weight:700;line-height:22px}
.feature-lead p{font-size:15px;line-height:23px;color:var(--muted);margin-top:12px}
.lead-icon{width:115px;height:115px;margin:0 auto 12px;border-radius:50%;background:linear-gradient(200deg,#1c1c1e 0%,#3a3a3c 45%,#bdbdbd 100%)}

/* sections */
.section-title{left:0;width:1200px;font-size:28px;font-weight:700}
.founders-text{left:208px;width:784px;top:1773px;font-size:15px;line-height:23px;color:#d8d8dc}
.founders-text p+p{margin-top:8px}

.stat{width:220px;text-align:center}
.stat b{display:block;font-size:54px;font-weight:700;line-height:1;background:linear-gradient(#d8d8d8,#8d8d8d);-webkit-background-clip:text;background-clip:text;color:transparent}
.stat span{display:block;font-size:18px;font-weight:400;line-height:23px;margin-top:6px}

.partner{width:180px;height:180px;border-radius:50%;background:radial-gradient(circle at 50% 8%,#5a5a5a,#1e1e1e 45%,#121212 70%,#2e2e2e 100%);display:flex;align-items:center;justify-content:center;font-size:22px;font-weight:600;color:#9d9d9d}

/* cta */
.cta-band{left:199px;top:3184px;width:796px;height:174px;border-radius:87px;background:linear-gradient(110deg,#1a1a1c,#232326 60%,#1b1b1d)}
.cta-title{left:258px;top:3240px;font-size:28px;font-weight:700}
.cta-sub{left:258px;top:3284px;font-size:15px;color:var(--muted)}
.cta-btn{left:825px;top:3255px;width:110px;height:35px}

/* footer */
.foot-logo{left:184px;top:3466px;font-size:38px;font-weight:700;line-height:1;letter-spacing:-.5px}
.foot-logo small{display:block;font-size:12px;letter-spacing:5px;font-weight:600;margin-top:2px}
.foot-contact{left:184px;top:3540px;font-size:13px;line-height:20px;font-style:normal}
.foot-links{left:469px;top:3480px;font-size:12px;line-height:24px}
.foot-links h4,.foot-news h4{font-size:16px;font-weight:700;line-height:19px;margin-bottom:6px}
.foot-news{left:680px;top:3482px}
.email{margin-top:10px;width:190px;height:35px;border:1.5px solid #fff;border-radius:18px;display:flex;align-items:center;justify-content:space-between;padding:0 12px 0 18px;font-size:11px}
.consent{display:flex;gap:8px;margin-top:12px;font-size:9px;line-height:11px;color:var(--muted)}
.consent i{width:13px;height:13px;border:1px solid #aaa;flex:none}
.socials{left:959px;top:3521px;display:flex;gap:10px}
.socials span{width:28px;height:28px;border-radius:50%;background:#1c1c1e;display:flex;align-items:center;justify-content:center}
.socials span::after{content:"";width:6px;height:6px;border-radius:50%;background:#fff}
.foot-rule{left:93px;top:3740px;width:1013px;height:1px;background:var(--line)}
.copyright{left:0;width:1200px;top:3761px;font-size:12px;color:#ccc}
.chat{left:1113px;top:3710px;width:56px;height:56px;border-radius:50%;background:var(--accent);display:flex;align-items:center;justify-content:center}
</style>
</head>
<body>
<div class="page">

  <svg class="backdrop" width="1200" height="3797" viewBox="0 0 1200 3797" aria-hidden="true">
    <defs>
      <radialGradient id="sphere" cx="50%" cy="100%" r="95%">
        <stop offset="0" stop-color="#5c5c5f"/>
        <stop offset=".35" stop-color="#2a2a2c"/>
        <stop offset=".75" stop-color="#111112"/>
        <stop offset="1" stop-color="#0c0c0d"/>
      </radialGradient>
      <linearGradient id="arcfill" x1="0" y1="0" x2="0" y2="1">
        <stop offset="0" stop-color="#1d1d1f"/>
        <stop offset=".3" stop-color="#0f0f10"/>
        <stop offset="1" stop-color="#0b0b0c"/>
      </linearGradient>
    </defs>
    <ellipse cx="600" cy="2600" rx="1100" ry="1160" fill="url(#arcfill)"/>
    <ellipse cx="620" cy="3300" rx="1000" ry="1280" fill="#0a0a0b"/>
    <ellipse cx="620" cy="3300" rx="1000" ry="1280" fill="none" stroke="#1a1a1c" stroke-width="2"/>
    <ellipse cx="600" cy="3700" rx="1050" ry="1030" fill="#0d0d0e"/>
    <circle cx="598" cy="1222" r="412" fill="url(#sphere)"/>
    <path d="M985 3228 C1080 3260 1150 3310 1200 3360 L1200 3450 C1150 3370 1070 3300 980 3260 Z" fill="var(--ring)"/>
    <path d="M55 3495 C110 3420 180 3360 240 3328" fill="none" stroke="#9a9a9a" stroke-width="2"/>
  </svg>

  <!-- hero imagery -->
  <svg class="abs" style="left:0;top:0" width="1200" height="760" viewBox="0 0 1200 760">
    <defs>
      <linearGradient id="city" x1="0" y1="0" x2="0" y2="1">
        <stop offset="0" stop-color="#050505"/>
        <stop offset=".35" stop-color="#1a140d"/>
        <stop offset=".6" stop-color="#2c2217"/>
        <stop offset=".8" stop-color="#3a2b1a"/>
        <stop offset="1" stop-color="#171310"/>
      </linearGradient>
    </defs>
    <path role="img" aria-label="Night skyline of a city under a rising moon, hero video" d="M0 0 H1200 V560 C1060 640 960 690 884 720 C700 770 460 720 317 648 C180 570 70 460 0 368 Z" fill="url(#city)"/>
    <path d="M884 724 C980 700 1100 640 1200 570 L1200 592 C1100 665 990 720 884 742 Z" fill="var(--ring)"/>
    <path d="M85 490 C160 570 240 620 317 650" fill="none" stroke="#9a9a9a" stroke-width="3"/>
  </svg>

  <!-- nav -->
  <div class="abs nav-logo">Nocturne<small>VENTURES</small></div>
  <span class="abs nav-links" style="left:681px">Home</span>
  <span class="abs nav-links" style="left:763px">Join VC</span>
  <span class="abs nav-links" style="left:837px">Startups</span>
  <span class="abs nav-links" style="left:946px">Log In</span>
  <div class="abs nav-cta">Get Started</div>

  <h1 class="abs hero-title center">Venture Capital for the<br>late night hustlers</h1>
  <p class="abs hero-sub center">Become a Venture Capital Investor</p>
  <a class="abs btn hero-btn">Learn More</a>

  <!-- become a VC -->
  <div class="abs become-card center">
    <div class="become-glow" role="img" aria-label="Soft blue light trail"></div>
    <h2 class="become-title">Become a VC</h2>
    <p class="become-text">At Nocturne Ventures, we're opening the doors to a new kind of investor, mid-career professionals and aspiring VCs who want real skin in the game, not just exposure from the sidelines.</p>
  </div>

  <!-- features -->
  <div class="abs feature" style="left:43px;top:1157px">
    <div class="feature-icon" role="img" aria-label="Icon: handshake on a grey disc"></div>
    <h3>Hands on<br>VC Work</h3>
  </div>
  <div class="abs feature" style="left:267px;top:1157px">
    <div class="feature-icon" role="img" aria-label="Icon: hand holding a growing plant on a grey disc"></div>
    <h3>Earn Carry and Put Your<br>Name on an Investment</h3>
  </div>
  <div class="abs feature-lead" style="left:515px;top:1122px">
    <div class="lead-icon" role="img" aria-label="Icon: growth chart held in a hand, set in a crescent"></div>
    <h3>Meaningful Opportunities to<br>develop your career in Venture Capital</h3>
    <p>Nocturne Investors, depending on the level of commitment and involvement, can work at our fund as Partners, Principals, Senior Associates, Associates and Venture Partners.</p>
  </div>
  <div class="abs feature" style="left:920px;top:1157px">
    <div class="feature-icon" role="img" aria-label="Icon: community of people around a leader on a grey disc"></div>
    <h3>Join a community<br>of Hustlers</h3>
  </div>

  <!-- founders -->
  <div class="abs" role="img" aria-label="Red particle wave, left" style="left:0;top:1800px;width:440px;height:260px;background:radial-gradient(ellipse 60% 40% at 40% 50%,rgba(200,60,50,.22),transparent 70%)"></div>
  <div class="abs" role="img" aria-label="Red particle wave, right" style="left:740px;top:1880px;width:460px;height:400px;background:radial-gradient(ellipse 55% 40% at 55% 45%,rgba(210,70,60,.22),transparent 70%)"></div>
  <h2 class="abs section-title center" style="top:1727px">Simplifying success for founders</h2>
  <div class="abs founders-text center">
    <p>Our strength lies in our network. Our LPs and operating partners are all mid-to-senior level executives in their industries. They bring real-world corporate experience, offering strategic insights and operational support to help our portfolio companies scale efficiently.</p>
    <p>We cut through the noise and get to the core of your business fast. If we love what you're building, we'll move. If not, we'll tell you quickly and respectfully. That lets you make</p>
  </div>
  <a class="abs btn" style="left:545px;top:1909px;width:110px;height:34px">Learn More</a>

  <!-- fund economics -->
  <h2 class="abs section-title center" style="top:2270px">Fund Economics</h2>
  <div class="abs stat" style="left:77px;top:2374px"><b>14</b><span>Pre-Seed /<br>Seed Investments</span></div>
  <div class="abs stat" style="left:285px;top:2374px"><b>50K</b><span>Check Size</span></div>
  <div class="abs stat" style="left:496px;top:2374px"><b>20%</b><span>Carried Interest</span></div>
  <div class="abs stat" style="left:720px;top:2374px"><b>2.5%</b><span>Management Fee</span></div>
  <div class="abs stat" style="left:939px;top:2374px"><b>1M</b><span>Fund Size</span></div>
  <div class="abs" role="img" aria-label="Blue light bars rising like a sound wave" style="left:0;top:2505px;width:1200px;height:210px;background:linear-gradient(180deg,transparent,rgba(90,100,170,.28) 45%,rgba(60,70,130,.18) 75%,transparent)"></div>

  <!-- partners -->
  <h2 class="abs section-title center" style="top:2847px">Our Partners</h2>
  <div class="abs partner" style="left:202px;top:2908px">Altrive</div>
  <div class="abs partner" style="left:408px;top:2908px">Corvale</div>
  <div class="abs partner" style="left:613px;top:2908px">Brisklane</div>
  <div class="abs partner" style="left:819px;top:2908px">Tessaro</div>

  <!-- cta -->
  <div class="abs cta-band" role="img" aria-label="Dark band with faint dotted grid"></div>
  <h2 class="abs cta-title">Ready to start investing as a VC?</h2>
  <p class="abs cta-sub">Book an interview to learn more and see if you qualify.</p>
  <a class="abs btn cta-btn">Get Started</a>

  <!-- footer -->
  <div class="abs foot-logo">Nocturne<small>VENTURES</small></div>
  <address class="abs foot-contact">415-555-0148<br>hello@nocturnevc.example<br>218 Harlow Ave<br>San Francisco, CA 94158</address>
  <div class="abs foot-links"><h4>Useful Links</h4>Solutions<br>Vision<br>Programs<br>Blog<br>Get Started</div>
  <div class="abs foot-news">
    <h4>Subscribe to<br>Our Newsletter</h4>
    <div class="email"><span>Email</span>
      <svg width="12" height="12" viewBox="0 0 12 12"><path d="M1 6 L11 1 L7 11 L6 7 Z" fill="none" stroke="#fff" stroke-width="1.2" stroke-linejoin="round"/></svg>
    </div>
    <div class="consent"><i></i><span>Yes, subscribe me to<br>your newsletter.*</span></div>
  </div>
  <div class="abs socials" aria-label="Social links"><span></span><span></span><span></span></div>

  <div class="abs foot-rule"></div>
  <p class="abs copyright center">©Copyright 2025 | All Rights Reserved</p>
  <div class="abs chat" aria-label="Chat">
    <svg width="28" height="26" viewBox="0 0 28 26"><path d="M14 2 C21 2 26 6.5 26 12 C26 17.5 21 22 14 22 L8 25 L9 20.5 C4.5 18.8 2 15.6 2 12 C2 6.5 7 2 14 2 Z" fill="#1a1a1a"/><circle cx="9" cy="12" r="1.6" fill="#fff"/><circle cx="14" cy="12" r="1.6" fill="#fff"/><circle cx="19" cy="12" r="1.6" fill="#fff"/></svg>
  </div>
</div>
</body>
</html>
```